I am looking for a Business Card Design for my spirit company titled "Harbor Pour Co" The company specializes in prohibition style/speakeasy mixology drinks and alcohol distribution. I am looking for Retro, Masculine, Sophisticated Card that embodies the look of Prohibition. Black and White colors. Also add Facebook, Instgram logo

Information that should go on the card is my Name, Title, Phone, Email, Website as follows:

Tobias K Verran
Principal
301.555.0187
tobias@harborpourco.example
harborpourco.example
Updates

Hello all I have uploaded a pdf version of the logo. It seems as if some are saying the resolution is too small.

Target Market(s)

Male and Female drinkers of all ages with a sophisticated palate that have an appreciation for fine crafted cocktail

Industry/Entity Type

Business

Requirements
Must have
• Information that should go on the card is my Name, Title, Phone, Email, Website as follows:

Tobias K Verran
Principal
301.555.0187
tobias@harborpourco.example
harborpourco.example

```html
<!DOCTYPE html>
<html lang="en">
<head>
<meta charset="utf-8">
<title>Harbor Pour Co – Business Card</title>
<link rel="stylesheet" href="https://fonts.googleapis.com/css2?family=Rubik+Dirt&display=swap">
<style>
  :root {
    --page-bg: #e4e1dc;
    --card-white: #ffffff;
    --ink: #141414;
    --band-black: #0d0d0d;
    --band-grey: #2a2a2a;
    --paper-text: #f2f2f2;
    --ring-grey: #d4d6d8;
  }
  * { margin: 0; padding: 0; box-sizing: border-box; }
  html, body {
    width: 1200px;
    height: 1200px;
    overflow: hidden;
    background: var(--page-bg);
  }
  .sheet {
    position: relative;
    width: 1200px;
    height: 1200px;
  }
  .card {
    position: absolute;
    left: 110px;
    width: 980px;
    height: 570px;
    background: var(--card-white);
    overflow: hidden;
  }
  .card--front { top: 18px; }
  .card--back { top: 612px; }

  .holder {
    position: absolute;
    left: 54px;
    top: 140px;
    font-family: "Rubik Dirt", "Impact", sans-serif;
    color: var(--ink);
  }
  .holder__name {
    font-size: 44px;
    line-height: 1;
    letter-spacing: 0.5px;
  }
  .holder__title {
    margin-top: 8px;
    font-size: 23px;
    line-height: 1;
  }

  .brand {
    position: absolute;
    display: flex;
    align-items: center;
    justify-content: center;
  }
  .brand__ring {
    position: absolute;
    border-radius: 50%;
    border: 10px solid var(--ring-grey);
  }
  .brand__name {
    position: relative;
    font-family: "Rubik Dirt", "Impact", sans-serif;
    color: var(--ink);
    white-space: nowrap;
  }
  .card--front .brand {
    left: 612px; top: 36px; width: 276px; height: 276px;
  }
  .card--front .brand__ring { inset: 0; }
  .card--front .brand__name { font-size: 36px; }
  .card--back .brand {
    left: 324px; top: 126px; width: 320px; height: 320px;
  }
  .card--back .brand__ring { inset: 0; }
  .card--back .brand__name { font-size: 44px; }

  .contact-band {
    position: absolute;
    left: 0;
    bottom: 0;
    width: 980px;
    height: 236px;
  }
  .contact-band svg { display: block; }
  .contact-list {
    position: absolute;
    left: 54px;
    top: 60px;
    list-style: none;
    font-family: "Rubik Dirt", "Impact", sans-serif;
    color: var(--paper-text);
    font-size: 27px;
    line-height: 48px;
    letter-spacing: 0.5px;
  }
  .social {
    position: absolute;
    right: 30px;
    bottom: 28px;
    display: flex;
    gap: 12px;
  }
  .social__badge {
    width: 32px;
    height: 32px;
    border-radius: 5px;
    background: var(--paper-text);
  }
</style>
</head>
<body>
<main class="sheet">

  <section class="card card--front">
    <div class="holder">
      <p class="holder__name">Tobias K Verran</p>
      <p class="holder__title">Principal</p>
    </div>

    <div class="brand">
      <span class="brand__ring"></span>
      <span class="brand__name">Harbor Pour Co</span>
    </div>

    <div class="contact-band">
      <svg width="980" height="236" viewBox="0 0 980 236" aria-hidden="true">
        <defs>
          <radialGradient id="bandTone" cx="0.3" cy="0.7" r="0.9">
            <stop offset="0" stop-color="#2e2e2e"/>
            <stop offset="1" stop-color="#0b0b0b"/>
          </radialGradient>
        </defs>
        <path fill="url(#bandTone)" d="M0 14 L22 10 L40 16 L63 8 L88 14 L110 9 L135 15 L160 7 L188 13 L214 9 L240 16 L268 8 L296 13 L322 10 L350 15 L378 7 L404 12 L432 9 L460 15 L488 8 L514 13 L542 10 L570 16 L598 8 L626 12 L652 9 L680 15 L708 7 L736 13 L762 10 L790 15 L818 8 L846 13 L872 9 L900 15 L928 8 L954 12 L980 10 L980 236 L0 236 Z"/>
      </svg>
      <ul class="contact-list">
        <li>Phone : 301.555.0187</li>
        <li>Email : tobias@harborpourco.example</li>
        <li>Web : www.harborpourco.example</li>
      </ul>
      <div class="social">
        <span class="social__badge" role="img" aria-label="Social network link"></span>
        <span class="social__badge" role="img" aria-label="Photo sharing link"></span>
      </div>
    </div>
  </section>

  <section class="card card--back">
    <div class="brand">
      <span class="brand__ring"></span>
      <span class="brand__name">Harbor Pour Co</span>
    </div>
  </section>

</main>
</body>
</html>
```